Paleo Diet Book Cover Design

I need a cover designed for my book Stone Frame that will be sold on Rivora Pageleaf and other sites. So the front, side and back will need to be designed. I have attached part of the book here so feel free to skim through the content and give it a quick read to get a feel for what the book is about. Stone Frame is about eating the diet of the caveman (paleolithic era-paleo) and a 12 week workout plan with a grocery shopping list and meal plans. It is for men and women ages 18+ who are interested in health and fitness and becoming healthier overall.
The graphics should be secondary, and it should add to the text, not distract from it. This is even more important because the size of the cover displayed on Rivora/Pageleaf, when your book is first seen by a potential buyer, is so tiny. It's barely an inch high, and even smaller in width.
So the words have to be big, bold, benefit-rich and easy to read. That also means, don't mess with the fancy fonts. Clean, clear, crisp font is best. And, did I say BIG already?
Contrast the colors of the text and background, so its even easier to read. That means, dark text on light background or visa versa. Colors like darker reds, blues / teals and oranges.
Please read this: http://www.bookvantrel.com/8-cover-design-secrets-publishers-use-to-manipulate-readers-into-buying-books/
The cover has to be bold and easy to read, it has to stick out, it has to draw the attention of your readers so that they zero in on my book, out of all the other books on the page. (Much like they would when viewing a classified ads site/page.)
The Title of the Book is Stone Frame, and the subtitle is "Transform Your Body For Life in 12 Weeks With Proven Workouts and Paleo Diet Based Nutrition" Perhaps “Transform Your Body For Life in 12 Weeks” could also be in a large font similar to the title with the rest of the subtitle following afterwards. You can try having the title be the smaller font with the subtitle being the larger font as well.
Then the authors name "Colin Marsh” incorporated into the design.
I am not sure what to use as the background type of design for the front of the book so feel free to be creative with that.
The size needs to be 1563 pixels on the shortest side and 2500 pixels on the longest side just for the front of the cover.

```html
<!DOCTYPE html>
<html lang="en">
<head>
<meta charset="utf-8">
<title>Stone Frame – Colin Marsh</title>
<link rel="stylesheet" href="https://fonts.googleapis.com/css2?family=Cinzel:wght@700;900&family=Oswald:wght@400;500&family=Roboto+Condensed:ital,wght@1,400&family=Open+Sans:wght@800&display=swap">
<style>
  :root {
    --sun-core: #ffee00;
    --sun-mid: #ffd400;
    --sun-edge: #ffb400;
    --veg-orange: #ff9a1a;
    --title-brown: #744a04;
    --ink: #111111;
    --tagline-grey: #4a4a4a;
  }
  html, body {
    margin: 0;
    padding: 0;
    overflow: hidden;
    background: #ffffff;
  }
  .cover {
    position: relative;
    width: 750px;
    height: 1200px;
    overflow: hidden;
    background: radial-gradient(circle at 51% 50%, var(--sun-core) 0%, var(--sun-mid) 45%, var(--sun-edge) 100%);
  }
  .veg-band {
    position: absolute;
    left: 0;
    width: 750px;
  }
  .veg-band--top {
    top: 0;
    height: 170px;
    background: linear-gradient(to bottom, rgba(255,150,20,0.75), rgba(255,170,20,0));
  }
  .veg-band--bottom {
    bottom: 0;
    height: 200px;
    background: linear-gradient(to top, rgba(255,150,20,0.8), rgba(255,170,20,0));
  }
  .author {
    position: absolute;
    top: 62px;
    left: 0;
    width: 750px;
    margin: 0;
    text-align: center;
    font-family: "Cinzel", serif;
    font-weight: 900;
    font-size: 62px;
    line-height: 70px;
    letter-spacing: 1px;
    color: var(--ink);
  }
  .title {
    position: absolute;
    top: 262px;
    left: 100px;
    width: 560px;
    height: 300px;
  }
  .title text {
    font-family: "Open Sans", sans-serif;
    font-weight: 800;
    font-size: 170px;
    fill: var(--title-brown);
    stroke: var(--ink);
    stroke-width: 2.5;
  }
  .subtitle {
    position: absolute;
    top: 640px;
    left: 0;
    width: 750px;
    margin: 0;
    text-align: center;
    font-family: "Oswald", sans-serif;
    font-weight: 400;
    color: var(--ink);
  }
  .subtitle__line {
    display: block;
    font-size: 56px;
    line-height: 70px;
    letter-spacing: -0.5px;
  }
  .subtitle__big {
    font-weight: 500;
    font-size: 86px;
  }
  .subtitle__mid {
    font-weight: 500;
    font-size: 68px;
  }
  .tagline {
    position: absolute;
    top: 900px;
    left: 0;
    width: 750px;
    margin: 0;
    text-align: center;
    font-family: "Roboto Condensed", sans-serif;
    font-style: italic;
    font-size: 46px;
    line-height: 66px;
    color: var(--tagline-grey);
  }
</style>
</head>
<body>
  <main class="cover">
    <div class="veg-band veg-band--top" role="img" aria-label="Orange silhouettes of root vegetables along the top edge"></div>
    <div class="veg-band veg-band--bottom" role="img" aria-label="Orange silhouettes of carrots and beets along the bottom edge"></div>

    <p class="author">COLIN<br>MARSH</p>

    <svg class="title" viewBox="0 0 560 300" aria-label="Stone Frame">
      <text x="0" y="126" textLength="555" lengthAdjust="spacingAndGlyphs">STONE</text>
      <text x="0" y="292" textLength="555" lengthAdjust="spacingAndGlyphs">FRAME</text>
    </svg>

    <h2 class="subtitle">
      <span class="subtitle__line">Transform Your Body</span>
      <span class="subtitle__line">For Life</span>
      <span class="subtitle__line">in <span class="subtitle__mid">12</span> <span class="subtitle__big">Weeks</span></span>
    </h2>

    <p class="tagline">“With Proven Workouts and<br>Paleo Diet Based Nutrition”</p>
  </main>
</body>
</html>
```